SKYTHRESH (drone photo and video) and Photogrammetry Services (mapping and 3D modeling)

We need a business card design for a SKYTHRESH. Our businesses provides (drone) Aerial Photo and Video Captures. However we also provide Photogrammetry (which is 3D modeling and mapping). We greatly value unique points of view taken of landscapes and subjects with aerial photography and videography. 3D modeling and mapping is the other area of focus and have an incredibly broad scope of applications and imaginative creativity.

Target Market(s)

Based out of Northern Virginia and serving the greater Virginia and Maryland areas

Industry/Entity Type

Drone Photo and video and Photogrammetry Services (mapping and 3D modeling)

Contact Information for Business Card

3D Models, Maps and Photo/Video Production name: Marcus Lindqvist email: mrl@skythresh.us website: skythresh.us phone: 571-308-6943; please also include "Aerial Photo/Video and 3D Mapping/Modeling"

Requirements
Must have
• Please make this design vertical and double sided. The selection box is not letting me choose Double Sided but that is my wish. Incorporate uploaded LOGO and color scheme
Nice to have
• Preferably does not feel too crowded and balances not having an exaggerated amount of distracting detail
Should not have
• do not cram bullet points or text in long form

```html
<!DOCTYPE html>
<html lang="en">
<head>
<meta charset="utf-8">
<title>SKYTHRESH Business Card</title>
<link rel="stylesheet" href="https://fonts.googleapis.com/css2?family=Montserrat:wght@600;700;800&family=Arimo:wght@400;700&display=swap">
<style>
  :root {
    --bg: #e9e7e4;
    --card: #ffffff;
    --ink: #111111;
    --muted: #555555;
    --red: #e8253a;
    --orange: #f4772a;
    --amber: #f9b024;
    --shadow: rgba(0, 0, 0, 0.18);
  }
  * { box-sizing: border-box; margin: 0; padding: 0; }
  html, body {
    width: 1200px;
    height: 941px;
    overflow: hidden;
    background: var(--bg);
  }
  .canvas {
    position: relative;
    width: 1200px;
    height: 941px;
    display: flex;
    justify-content: center;
    align-items: center;
    gap: 90px;
  }
  .card {
    position: relative;
    width: 370px;
    height: 610px;
    background: var(--card);
    box-shadow: 0 10px 30px var(--shadow);
    overflow: hidden;
  }
  .brand {
    position: absolute;
    left: 0;
    right: 0;
    display: flex;
    flex-direction: column;
    align-items: center;
  }
  .brand-dot {
    width: 96px;
    height: 96px;
    border-radius: 50%;
    background: var(--orange);
    margin-bottom: 14px;
  }
  .brand-name {
    font-family: "Montserrat", sans-serif;
    font-weight: 800;
    font-size: 36px;
    line-height: 42px;
    letter-spacing: 1px;
    color: var(--ink);
  }
  .brand-tagline {
    margin-top: 6px;
    font-family: "Montserrat", sans-serif;
    font-weight: 600;
    font-size: 11px;
    letter-spacing: 0.6px;
    color: var(--muted);
    white-space: nowrap;
  }
  /* front */
  .card-front .brand { top: 62px; }
  .contact {
    position: absolute;
    left: 46px;
    top: 272px;
  }
  .person-name {
    font-family: "Montserrat", sans-serif;
    font-weight: 700;
    font-size: 25px;
    line-height: 30px;
    color: var(--red);
    letter-spacing: 0.5px;
  }
  .person-role {
    font-family: "Montserrat", sans-serif;
    font-weight: 700;
    font-size: 19px;
    line-height: 24px;
    color: var(--ink);
    margin-top: 2px;
  }
  .contact-list {
    list-style: none;
    margin-top: 20px;
    font-family: "Arimo", sans-serif;
    font-size: 17px;
    color: var(--ink);
  }
  .contact-list li {
    display: flex;
    align-items: center;
    gap: 10px;
    line-height: 24px;
  }
  .contact-list svg { width: 14px; height: 14px; flex: none; }
  .wave {
    position: absolute;
    left: 0;
    top: 0;
    width: 370px;
    height: 610px;
  }
  .front-url {
    position: absolute;
    right: 24px;
    bottom: 46px;
    font-family: "Arimo", sans-serif;
    font-size: 19px;
    color: var(--ink);
  }
  /* back */
  .card-back .brand { top: 160px; }
  .back-url {
    position: absolute;
    left: 0;
    right: 0;
    top: 440px;
    text-align: center;
    font-family: "Arimo", sans-serif;
    font-weight: 700;
    font-size: 16px;
    letter-spacing: 5px;
    color: var(--ink);
  }
  .back-url .domain { color: var(--orange); }
</style>
</head>
<body>
<main class="canvas">

  <section class="card card-front" aria-label="Card front">
    <svg class="wave" viewBox="0 0 370 610" aria-hidden="true">
      <defs>
        <linearGradient id="waveFill" x1="0" y1="1" x2="1" y2="0">
          <stop offset="0" stop-color="#f9b024"/>
          <stop offset="0.5" stop-color="#f4772a"/>
          <stop offset="1" stop-color="#e8253a"/>
        </linearGradient>
      </defs>
      <path d="M0 555 C 130 566, 210 535, 248 455 C 275 398, 300 352, 370 338 L370 610 L0 610 Z" fill="url(#waveFill)"/>
      <path d="M0 549 C 130 560, 206 529, 244 449 C 271 392, 296 346, 370 332" fill="none" stroke="#111" stroke-width="5"/>
    </svg>

    <div class="brand">
      <div class="brand-dot"></div>
      <div class="brand-name">SKYTHRESH</div>
      <div class="brand-tagline">Aerial Photo/Video and 3D Mapping/Modeling</div>
    </div>

    <div class="contact">
      <div class="person-name">Marcus Lindqvist</div>
      <div class="person-role">President</div>
      <ul class="contact-list">
        <li>
          <svg viewBox="0 0 24 24"><path fill="#e8253a" d="M6.6 10.8a15.1 15.1 0 0 0 6.6 6.6l2.2-2.2c.3-.3.7-.4 1-.2 1.1.4 2.3.6 3.6.6.6 0 1 .4 1 1V20c0 .6-.4 1-1 1A17 17 0 0 1 3 4c0-.6.4-1 1-1h3.5c.6 0 1 .4 1 1 0 1.2.2 2.4.6 3.6.1.3 0 .7-.2 1z"/></svg>
          <span>571-308-6943</span>
        </li>
        <li>
          <svg viewBox="0 0 24 24"><path fill="#e8253a" d="M2 5h20v14H2z"/><path fill="none" stroke="#fff" stroke-width="2" d="M2 5l10 8 10-8"/></svg>
          <span>mrl@skythresh.us</span>
        </li>
      </ul>
    </div>

    <div class="front-url">www.skythresh.us</div>
  </section>

  <section class="card card-back" aria-label="Card back">
    <div class="brand">
      <div class="brand-dot"></div>
      <div class="brand-name">SKYTHRESH</div>
      <div class="brand-tagline">Aerial Photo/Video and 3D Mapping/Modeling</div>
    </div>
    <div class="back-url">www.<span class="domain">skythresh.us</span></div>
  </section>

</main>
</body>
</html>
```